Business Card Design

I would like a logo created for the top left corner of the card please. I would like a checkerboard in a dark navy with the edges fading out and one random bright orange square.
Updates

I have attached some further notes and a really rough sketch of what I am after.  Thank you. :)

Target Market(s)

Construction, mining, mechanical

Industry/Entity Type

Business

Contact Information for Business Card

Korvane Works Pty Ltd, Glen Hadwick, P. 0418365072, F. 0736209158, E.glen@korvaneworks.com.au, PO Box 87 YARRAWONGA Q 4581, ABN 53209874611

Font styles to use
Sans Serif

Requirements
Must have
• Really Dark Navy
Really bright Orange

```html
<!DOCTYPE html>
<html lang="en">
<head>
<meta charset="utf-8">
<title>Korvane Works Pty Ltd – Glen Hadwick</title>
<link rel="stylesheet" href="https://fonts.googleapis.com/css2?family=Roboto+Condensed:ital,wght@0,400;0,700;1,400;1,700&display=swap">
<style>
  :root {
    --navy: #0c3040;
    --orange: #ff7d0a;
    --paper: #ffffff;
  }
  html, body {
    margin: 0;
    padding: 0;
    overflow: hidden;
    background: var(--paper);
  }
  .card {
    position: relative;
    width: 1200px;
    height: 742px;
    background: var(--paper);
    color: var(--navy);
    font-family: "Roboto Condensed", "Arial Narrow", Arial, sans-serif;
    overflow: hidden;
  }
  .brand-mark {
    position: absolute;
    left: 0;
    top: 0;
    width: 427px;
    height: 414px;
    display: flex;
    align-items: center;
    justify-content: center;
    gap: 18px;
  }
  .brand-mark__square {
    width: 40px;
    height: 40px;
    background: var(--orange);
  }
  .brand-mark__name {
    font-size: 40px;
    font-weight: 700;
    color: var(--navy);
    white-space: nowrap;
  }
  .company {
    position: absolute;
    left: 515px;
    top: 98px;
    margin: 0;
    font-weight: 700;
    line-height: 1;
    white-space: nowrap;
  }
  .company__lead { font-size: 74px; }
  .company__rest { font-size: 44px; }
  .person {
    position: absolute;
    left: 517px;
    top: 300px;
    margin: 0;
    font-size: 48px;
    font-weight: 700;
    font-style: italic;
    line-height: 1;
  }
  .contact {
    position: absolute;
    left: 517px;
    top: 412px;
    margin: 0;
    padding: 0;
    list-style: none;
    font-size: 36px;
    font-style: italic;
    line-height: 51px;
    white-space: nowrap;
  }
</style>
</head>
<body>
  <main class="card">
    <div class="brand-mark">
      <span class="brand-mark__square"></span>
      <span class="brand-mark__name">Korvane Works</span>
    </div>

    <h1 class="company"><span class="company__lead">Korvane</span> <span class="company__rest">Works Pty Ltd</span></h1>

    <p class="person">Glen Hadwick</p>

    <ul class="contact">
      <li>P. 0418365072</li>
      <li>F. 0736209158</li>
      <li>E. Glen@korvaneworks.com.au</li>
      <li>PO Box 87 YARRAWONGA Q 4581, ABN</li>
      <li>53209874611</li>
    </ul>
  </main>
</body>
</html>
```